Thai Restruant Business Card Design

A Business card design for a Thai and Laos take away restaurant.

We are a highly respectable take away restaurant in a small shopping center.

The design must have a Papaya Tree and Thai Palace.

The final design should communicate, innovation, fun and delicious food.

Industry/Entity Type

Restaurant

Contact Information for Business Card

Mango Hearth, Thai & Lao Food, Shop 4. 71 Elm Lane. Cabramatta N.S.W 2166, Tel. 02-96415270, Open 7 Days From 8.30am To 6.30pm

```html
<!DOCTYPE html>
<html lang="en">
<head>
<meta charset="utf-8">
<title>Mango Hearth – Business Card</title>
<link href="https://fonts.googleapis.com/css2?family=Lora:wght@400;500&display=swap" rel="stylesheet">
<style>
  :root {
    --page-bg: #e9e4dc;
    --card-black: #0d0d0d;
    --card-charcoal: #2a2a2a;
    --gold: #e0b94e;
    --gold-light: #f1d88c;
    --gold-deep: #c79a32;
    --ink-white: #f4f1ea;
    --ink-dark: #1a1408;
    --palace-sky: #c9cfd6;
    --palace-gold: #b4862e;
    --palace-stone: #e6e2da;
  }
  * { box-sizing: border-box; margin: 0; padding: 0; }
  html, body {
    width: 1200px; height: 1023px; overflow: hidden;
    background: var(--page-bg);
  }
  .card {
    position: absolute; left: 150px; top: 254px;
    width: 900px; height: 514px;
    background: radial-gradient(ellipse at 40% 40%, var(--card-charcoal) 0%, var(--card-black) 75%);
    overflow: hidden;
    box-shadow: 0 14px 34px rgba(0,0,0,0.35);
    font-family: "Lora", Georgia, serif;
  }
  .brand {
    position: absolute; left: 120px; top: 62px;
    width: 460px;
  }
  .brand-name {
    display: flex; align-items: center; gap: 16px;
    color: var(--ink-white); font-size: 64px; font-weight: 400; line-height: 1;
    white-space: nowrap;
  }
  .brand-dot {
    width: 22px; height: 22px; border-radius: 50%; background: var(--gold);
    flex: none;
  }
  .brand-tagline {
    margin-top: 8px; margin-left: 236px;
    color: var(--ink-white); font-size: 22px; white-space: nowrap;
  }
  .details {
    position: absolute; left: 92px; top: 240px;
    color: var(--ink-white); font-size: 21px; line-height: 1.2;
  }
  .details .business { color: var(--gold); }
  .details .hours { margin-top: 26px; }
  .details .phone {
    display: flex; align-items: center; gap: 10px;
    font-size: 27px; margin-top: 2px;
  }
  .phone-icon { width: 24px; height: 24px; }
  .service-band {
    position: absolute; left: 0; bottom: 44px;
    width: 600px; height: 52px;
    background: linear-gradient(180deg, var(--gold-light), var(--gold) 55%, var(--gold-deep));
    display: flex; align-items: center; justify-content: center;
    color: var(--ink-dark); font-size: 24px;
  }
  .palace-photo {
    position: absolute; right: 0; top: 200px;
    width: 300px; height: 314px;
    background: linear-gradient(170deg, var(--palace-sky) 0%, var(--palace-gold) 40%, var(--palace-stone) 70%, #8c6a3a 100%);
  }
</style>
</head>
<body>
  <div class="card">
    <div class="brand">
      <div class="brand-name"><span class="brand-dot"></span>Mango Hearth</div>
      <div class="brand-tagline">Thai and Laos Food</div>
    </div>

    <div class="details">
      <p class="business">Mango Hearth, Thai &amp; Lao Food</p>
      <p>Shop 4. 71 Elm Lane Cabramatta</p>
      <p>N.S.W 2166</p>
      <p class="hours">Open 7 Days 8.30am to 6.30pm</p>
      <p class="phone">
        <svg class="phone-icon" viewBox="0 0 24 24" aria-hidden="true">
          <rect x="2" y="5" width="20" height="16" rx="4" fill="var(--gold)"/>
          <path d="M4 8 Q12 1 20 8 L18 11 Q12 6 6 11 Z" fill="var(--card-black)"/>
          <circle cx="12" cy="15" r="3.5" fill="var(--card-black)"/>
        </svg>
        02-96415270
      </p>
    </div>

    <div class="service-band">Thai and Laos Take Away Restaurant</div>

    <div class="palace-photo" role="img" aria-label="Photograph of a Thai royal palace with golden tiered spires and white walls"></div>
  </div>
</body>
</html>
```